Software Company Banner Ad

We need a banner ad in two sizes. 728x90 and 300x250.
They should have strong similarity to the following ads:
http://www.vexlo.net/search/results?brand[0]=quorp&ad=4821396
http://www.vexlo.net/search/results?brand[0]=dravensoft&ad=4830517
Idea will be very similar. We want the same grey color, white text, and a realistic owl that blinks. The owl should have dramatic, bright, yellow eyes. The text will animate "from the top" as in the example. Though the logo animation will be different, all text and non-logo animation should match the animation in the example advertisements. The text will rotate between the following four sentences and images.
Looking for a provider of procurement cloud apps?
[Images - attached below]
The experts really liked our KTV booth.
Get great results with every procurement. [Learn more]
There are three vector files attached below. Feel free to change the colors as necessary to match the color scheme of the ad. We need one 2013 and one 2014 award in the ad.
The awards could appear simultaneously, could swap with each other or could appear in succession. Animation is acceptable.
There is an additional vector file with the company logo. The company logo should go where the Quorp logo is in horizontal ad. The company logo should go where the Dravensoft logo is in the block ad. The example ad has two logos. We will only need one logo on our ads. The logo should be changed to the color of the text used for the ad (white).
The owls eyes should slowly blink two times (as in the example).
The owl eyes should immediately grab someone's attention and all colors should compliment these eyes.
The [Learn more] button should have animation. The button should match the color of the owl's eyes. There should be a line/gleam/glare of light that travels across the button. The button should be embossed with the subtle animation occurring each time it appears.
Ads should be done with flash. We will need the source files and the names of any fonts used at the end of the project.
Thank you and please do not hesitate to contact with any questions.
Reason: We have contacted several photographers to see if the alternative owl images are available on Pixvane, Framelodge or similar. The duration extension is to accommodate this.
Target Market(s)
Target customers are procurement department employees of large companies.
Industry/Entity Type
It Company

```html
<!DOCTYPE html>
<html lang="en">
<head>
<meta charset="utf-8">
<title>Norva banner ads</title>
<link rel="stylesheet" href="https://fonts.googleapis.com/css2?family=Roboto:wght@400;500;700&display=swap">
<style>
  :root {
    --canvas: #ffffff;
    --band-grey: #7e7e7e;
    --text-white: #ffffff;
    --button-yellow: #f2c811;
    --button-yellow-dark: #d9b000;
    --button-ink: #333333;
    --photo-light: #b9b7b2;
    --photo-mid: #8d8a85;
    --photo-dark: #5e5b57;
  }
  * { margin: 0; padding: 0; box-sizing: border-box; }
  html, body {
    width: 1200px;
    height: 574px;
    overflow: hidden;
    background: var(--canvas);
    font-family: "Roboto", Arial, sans-serif;
  }
  .stage {
    position: relative;
    width: 728px;
    height: 348px;
    transform: scale(1.6484);
    transform-origin: 0 0;
  }

  /* Shared pieces */
  .headline {
    color: var(--text-white);
    font-weight: 400;
    text-align: center;
    line-height: 1.3;
    white-space: nowrap;
  }
  .headline strong { font-weight: 700; }
  .learn-more {
    position: absolute;
    display: flex;
    align-items: center;
    justify-content: center;
    gap: 8px;
    background: linear-gradient(180deg, var(--button-yellow) 0%, var(--button-yellow) 60%, var(--button-yellow-dark) 100%);
    border-radius: 4px;
    box-shadow: inset 0 1px 0 rgba(255,255,255,0.45), 0 1px 1px rgba(0,0,0,0.25);
    color: var(--button-ink);
    font-weight: 500;
    text-decoration: none;
    white-space: nowrap;
  }
  .learn-more svg { display: block; }
  .brand {
    position: absolute;
    display: flex;
    align-items: center;
    gap: 6px;
    color: var(--text-white);
    font-weight: 700;
    font-size: 18px;
    line-height: 1;
  }
  .brand-square {
    width: 10px;
    height: 10px;
    background: var(--text-white);
  }
  .owl-photo {
    position: absolute;
    background: radial-gradient(ellipse at 50% 45%, var(--photo-light) 0%, var(--photo-mid) 55%, var(--photo-dark) 100%);
  }

  /* 300 x 250 block */
  .ad-block {
    position: absolute;
    left: 0;
    top: 0;
    width: 300px;
    height: 250px;
    background: var(--band-grey);
    overflow: hidden;
  }
  .ad-block .owl-photo { left: 0; top: 0; width: 300px; height: 138px; }
  .ad-block .headline {
    position: absolute;
    left: 0; top: 143px; width: 300px;
    font-size: 20px;
  }
  .ad-block .learn-more {
    left: 10px; top: 207px; width: 151px; height: 34px;
    font-size: 19px;
  }
  .ad-block .brand { left: 196px; top: 216px; }

  /* 728 x 90 leaderboard */
  .ad-leaderboard {
    position: absolute;
    left: 0;
    top: 258px;
    width: 728px;
    height: 90px;
    background: var(--band-grey);
    overflow: hidden;
  }
  .ad-leaderboard .brand { left: 14px; top: 7px; }
  .ad-leaderboard .headline {
    position: absolute;
    left: 115px; top: 13px; width: 270px;
    font-size: 23px;
    line-height: 1.4;
  }
  .ad-leaderboard .learn-more {
    left: 391px; top: 30px; width: 137px; height: 31px;
    font-size: 17px;
  }
  .ad-leaderboard .owl-photo {
    left: 548px; top: 0; width: 180px; height: 90px;
    -webkit-mask-image: linear-gradient(90deg, transparent 0%, #000 22%);
    mask-image: linear-gradient(90deg, transparent 0%, #000 22%);
  }
</style>
</head>
<body>
<div class="stage">

  <section class="ad-block" aria-label="Norva 300 by 250 banner">
    <div class="owl-photo" role="img" aria-label="Photograph of an owl with bright yellow eyes looking straight ahead"></div>
    <p class="headline">Get great <strong>results</strong> with<br>every <strong>procurement</strong></p>
    <a class="learn-more" href="#">Learn more
      <svg width="18" height="18" viewBox="0 0 18 18" aria-hidden="true">
        <circle cx="9" cy="9" r="9" fill="var(--button-ink)"/>
        <path d="M7 5.2 L12.6 9 L7 12.8 Z" fill="var(--button-yellow)"/>
      </svg>
    </a>
    <div class="brand"><span class="brand-square" aria-hidden="true"></span>Norva</div>
  </section>

  <section class="ad-leaderboard" aria-label="Norva 728 by 90 banner">
    <div class="brand"><span class="brand-square" aria-hidden="true"></span>Norva</div>
    <p class="headline">Get great <strong>results</strong> with<br>every <strong>procurement</strong></p>
    <a class="learn-more" href="#">Learn more
      <svg width="17" height="17" viewBox="0 0 18 18" aria-hidden="true">
        <circle cx="9" cy="9" r="9" fill="var(--button-ink)"/>
        <path d="M7 5.2 L12.6 9 L7 12.8 Z" fill="var(--button-yellow)"/>
      </svg>
    </a>
    <div class="owl-photo" role="img" aria-label="Photograph of an owl with bright yellow eyes, fading into the grey band"></div>
  </section>

</div>
</body>
</html>
```